Informational Business Handout needs Company Information

We have this informational handout that we would like to start handing out to clients; however, the original designer failed to include any of our company contact information. Our main request is that you redesign this card with the appropriate contact information as listed below. We would like the information/content that is currently on the card to be on the new design as well. Feel free to take liberty with the rest of the card design, or not. Please see the card specifications and our company contact information below.

Card details: 7 x 5 inches (17.78 x 12.5 cm). Cardstock.

Company Contact Details:
Dorian Welkett, JD
TarnwickLaw, PLLC
482 E. Marlowe Ave, Ste. 310, St. George, UT 84770
hello@tarnwicklaw-mail.com
(435) 555-0147

```html
<!DOCTYPE html>
<html lang="en">
<head>
<meta charset="utf-8">
<title>Third-Party Supplemental Needs Trust Handout – TarnwickLaw</title>
<link href="https://fonts.googleapis.com/css2?family=Montserrat:wght@400;500;600;700;800&display=swap" rel="stylesheet">
<style>
  :root {
    --navy: #1f3461;
    --navy-soft: #2c4470;
    --blush: #f0e3df;
    --copper: #a0522d;
    --ink: #222222;
    --grey: #3a3a3a;
    --stage: #e9e9ec;
    --white: #ffffff;
  }
  * { margin: 0; padding: 0; box-sizing: border-box; }
  html, body { width: 1200px; height: 997px; overflow: hidden; }
  body {
    background: var(--stage);
    font-family: "Montserrat", Arial, sans-serif;
    position: relative;
  }
  .card-frame {
    position: absolute;
    left: 40px; top: 98px;
    width: 1120px; height: 800px;
  }
  .card {
    position: absolute; left: 0; top: 0;
    width: 1050px; height: 750px;
    background: var(--white);
    transform: scale(1.0667);
    transform-origin: 0 0;
    overflow: hidden;
    box-shadow: 0 4px 18px rgba(0,0,0,0.12);
  }
  .accent-panel { position: absolute; left: 0; top: 0; }
  .headline {
    position: absolute;
    color: var(--navy);
    font-weight: 800;
    text-transform: uppercase;
  }
  .headline--left { left: 61px; top: 40px; width: 430px; font-size: 33px; line-height: 40px; }
  .headline--right { left: 556px; top: 36px; width: 440px; font-size: 35.5px; line-height: 42px; }
  .intro {
    position: absolute; left: 61px; top: 206px; width: 416px;
    font-size: 17.4px; line-height: 22px; color: var(--ink);
    letter-spacing: 0.25px;
    text-align: justify;
  }
  .checklist { position: absolute; left: 558px; top: 135px; width: 422px; list-style: none; }
  .checklist li {
    position: relative; padding-left: 37px;
    font-size: 19px; line-height: 23px; font-weight: 600;
    color: var(--navy-soft); margin-bottom: 19px;
  }
  .checklist li::before {
    content: ""; position: absolute; left: 1px; top: 5px;
    width: 17px; height: 17px; border: 2.5px solid var(--navy);
  }
  .firm-mark {
    position: absolute; left: 540px; top: 412px; width: 450px;
    display: flex; align-items: center; gap: 18px;
  }
  .firm-mark__square { width: 40px; height: 40px; background: var(--navy); flex: none; }
  .firm-mark__name {
    font-size: 34px; font-weight: 700; color: var(--navy);
  }
  .attorney-name {
    position: absolute; left: 59px; top: 466px;
    font-size: 35px; font-weight: 700; color: var(--navy);
  }
  .divider {
    position: absolute; left: 60px; top: 523px; width: 934px; height: 2px;
    background: var(--copper);
  }
  .contact-list { position: absolute; left: 60px; top: 544px; list-style: none; }
  .contact-list li {
    display: flex; align-items: center; gap: 12px;
    font-size: 23px; line-height: 32px; color: var(--grey);
  }
  .contact-list svg { width: 19px; height: 19px; fill: var(--navy); flex: none; }
  .office-address {
    position: absolute; right: 53px; top: 544px; text-align: right;
    font-style: normal; font-size: 23px; line-height: 32px; color: var(--grey);
  }
  .office-address strong { color: var(--navy-soft); font-weight: 700; font-size: 24px; }
  .call-to-action {
    position: absolute; left: 0; top: 673px; width: 1050px; height: 77px;
    background: var(--navy); color: var(--white);
    display: flex; align-items: center; justify-content: center;
    text-align: center; font-size: 15.5px; line-height: 19px; font-weight: 500;
  }
</style>
</head>
<body>
  <div class="card-frame">
    <article class="card">
      <svg class="accent-panel" width="1050" height="750" viewBox="0 0 1050 750" aria-hidden="true">
        <path d="M477 0 H1050 V308 L700 383 Q585 408 548 338 Z" fill="var(--blush)"/>
      </svg>

      <h1 class="headline headline--left">Is a third-party supplemental needs trust necessary for your estate plan?</h1>
      <p class="intro">Will one of your intended beneficiaries have a recognized disability as determined by the social security administration thar renders the beneficiary unable to engage in any substantial gainful activity by reason of any medically determined physical or mental impairment which can be expected to result in death or which has lasted or can be expected to last for a continuous period of not less than twelve monts?</p>

      <h2 class="headline headline--right">Does the intended beneficiary...</h2>
      <ul class="checklist">
        <li>Currently receive or will be applying for social social security income?</li>
        <li>Currently receive, or<br>plan to apply for medicaid?</li>
        <li>Want to maintain or qualify for social security income &amp; or medicaid after benefitting from an inheritance?</li>
      </ul>

      <div class="firm-mark">
        <span class="firm-mark__square"></span>
        <span class="firm-mark__name">TarnwickLaw</span>
      </div>

      <p class="attorney-name">DORIAN WELKETT, JD</p>
      <div class="divider"></div>

      <ul class="contact-list">
        <li>
          <svg viewBox="0 0 24 24" aria-hidden="true"><path d="M6.6 10.8a15.1 15.1 0 0 0 6.6 6.6l2.2-2.2a1 1 0 0 1 1-.25 11.4 11.4 0 0 0 3.6.57 1 1 0 0 1 1 1V20a1 1 0 0 1-1 1A17 17 0 0 1 3 4a1 1 0 0 1 1-1h3.5a1 1 0 0 1 1 1c0 1.25.2 2.45.57 3.57a1 1 0 0 1-.25 1z"/></svg>
          (435) 555-0147
        </li>
        <li>
          <svg viewBox="0 0 24 24" aria-hidden="true"><path d="M2 5h20v14H2z M3.5 6.5 12 13l8.5-6.5" fill="var(--navy)" stroke="#fff" stroke-width="1.4"/></svg>
          hello@tarnwicklaw-mail.com
        </li>
        <li>
          <svg viewBox="0 0 24 24" aria-hidden="true"><circle cx="12" cy="12" r="10"/><path d="M2 12h20M12 2c3 3.2 3 16.8 0 20M12 2c-3 3.2-3 16.8 0 20" fill="none" stroke="#fff" stroke-width="1.3"/></svg>
          www.tarnwicklaw.example
        </li>
      </ul>

      <address class="office-address">
        <strong>TarnwickLaw, PLLC</strong><br>
        482 E. Marlowe Ave, Ste. 310<br>
        St. George, UT 84770
      </address>

      <p class="call-to-action">if you have an intended beneficiary with a recognized disability and you answered yes to any of these questions,<br>you should contact our office to discuss whether a Third-party Supplemental Needs Trust is right for your estate plan.</p>
    </article>
  </div>
</body>
</html>
```